Sale hospital laugh

With our Customer Tarno Athletic we have the opportunity to sell our Brand VUX Smart Sportswear in a Hopital. Now we need a flyer for the hopital which they can distribute to their employees. Please use font: Univers LT Std 45 Light or Univers LT Std 55 "180206_NK_Poster_A3_Staff_action.compressed" 180306_ZO_Flyer Content "As well as you find the the logos.

```html
<!DOCTYPE html>
<html lang="de">
<head>
<meta charset="utf-8">
<title>Mitarbeiteraktion – Spital Halden</title>
<link rel="stylesheet" href="https://fonts.googleapis.com/css2?family=Roboto:wght@300;400;700&display=swap">
<style>
  :root {
    --stage: #e6e6e6;
    --photo-light: #e4e4e4;
    --photo-mid: #c9c9c9;
    --photo-dark: #a9a9a9;
    --brand-blue: #0d3a86;
    --action-yellow: #fbe900;
    --ink: #111111;
    --paper: #ffffff;
    --callout: rgba(255, 255, 255, 0.82);
  }
  * { box-sizing: border-box; margin: 0; padding: 0; }
  html, body {
    width: 1200px; height: 1200px; overflow: hidden;
    background: var(--stage);
    font-family: "Roboto", Arial, sans-serif;
  }
  .poster {
    position: absolute; left: 194px; top: 30px;
    width: 812px; height: 1140px;
    background: var(--paper);
    overflow: hidden;
  }
  .hero-photo {
    position: absolute; left: 0; top: 0; width: 812px; height: 886px;
    background:
      radial-gradient(ellipse 320px 420px at 470px 460px, rgba(40,40,40,0.35), rgba(40,40,40,0) 70%),
      linear-gradient(180deg, var(--photo-light) 0%, var(--photo-mid) 55%, var(--photo-dark) 100%);
  }
  .shapes { position: absolute; left: 0; top: 0; width: 812px; height: 886px; }
  .discount {
    position: absolute; left: 44px; top: 110px;
    color: var(--paper); font-weight: 700; font-size: 38px; letter-spacing: 0.5px;
  }
  .callout-text {
    position: absolute; left: 440px; top: 654px; width: 310px;
    text-align: center; color: var(--ink); line-height: 1.2;
  }
  .callout-text .lead { font-weight: 700; font-size: 19px; }
  .callout-text .detail { font-weight: 400; font-size: 16px; margin-top: 2px; }
  .event-info {
    position: absolute; left: 200px; top: 818px; width: 420px; text-align: center;
  }
  .event-info .date { color: var(--action-yellow); font-size: 19px; font-weight: 400; }
  .event-info .sep { display: inline-block; width: 2px; height: 14px; background: var(--action-yellow); margin: 0 8px; vertical-align: -1px; }
  .event-info .place { color: var(--paper); font-size: 29px; font-weight: 700; margin-top: 2px; }
  .action-band {
    position: absolute; left: 0; top: 886px; width: 812px; height: 92px;
    background: var(--action-yellow);
    display: flex; align-items: center; justify-content: center;
    font-size: 35px; color: var(--ink); font-weight: 300;
  }
  .action-band strong { font-weight: 700; }
  .partners {
    position: absolute; left: 0; top: 978px; width: 812px; height: 162px;
    display: flex; align-items: center; justify-content: space-around; padding: 0 100px;
  }
  .partner {
    font-size: 30px; font-weight: 700; color: var(--ink);
    text-align: center; white-space: nowrap;
  }
</style>
</head>
<body>
  <main class="poster">
    <div class="hero-photo" role="img" aria-label="Studiofoto eines Läufers in dunklem Shirt, Kompressionstights und Laufschuhen im Sprint vor grauem Hintergrund"></div>

    <svg class="shapes" viewBox="0 0 812 886" aria-hidden="true">
      <polygon class="discount-flag" points="0,104 303,88 301,174 0,164" fill="var(--brand-blue)"/>
      <polygon class="callout-shape" points="433,634 778,634 718,747 493,794" fill="var(--callout)"/>
      <polygon class="event-plate" points="218,797 603,797 620,886 200,886" fill="var(--ink)"/>
    </svg>

    <div class="discount">20% RABATT</div>

    <div class="callout-text">
      <p class="lead">FÜR EIN EINZIGARTIGES<br>LAUFGEFÜHL:</p>
      <p class="detail">VUX COMPRESSIONSOCKS<br>UND VEYRA-AIR</p>
    </div>

    <div class="event-info">
      <p class="date">25. APRIL 2018<span class="sep"></span>10.00 - 14.00 UHR</p>
      <p class="place">MARCH</p>
    </div>

    <div class="action-band">MITARBEITERAKTION –&nbsp;<strong>SPITAL HALDEN</strong></div>

    <footer class="partners">
      <div class="partner partner-vux">VUX</div>
      <div class="partner partner-tarno">Tarno Athletic</div>
      <div class="partner partner-veyra">Veyra</div>
    </footer>
  </main>
</body>
</html>
```